Tidewater Guest Consulting

I am an independent operator engaged on short/medium term consultancy briefs within the Hotel/Resort sector in the Pacific Area and have a representation in Fiji.

A broad based services is offered and includes:

Development Advisory
Property Management
Sales & Marketing
Holiday Ownership/Timeshare
Resorts/Apartments/Motels/Flashpackers/B&B
Financial & Legal Referrals

Industry/Entity Type

Hotel

Contact Information for Business Card

Business name - TIDEWATER GUEST CONSULTING
My name - Marcus Holt
Address: PO Box 318 Coral Heath 4871 Qld
Phone: Australia: +61 7 55019284 Mobile: 0414093857 (Viber)
Fiji: +679 8230519
Email: marcuswholt@tealnest-mail.com

```html
<!DOCTYPE html>
<html lang="en">
<head>
<meta charset="utf-8">
<title>Tidewater Guest Consulting – Business Card</title>
<link href="https://fonts.googleapis.com/css2?family=Aldrich&display=swap" rel="stylesheet">
<style>
  :root {
    --backdrop: #d8d8da;
    --card-white: #ffffff;
    --card-charcoal: #333335;
    --brand-red: #e2262d;
    --text-light: #f2f2f2;
  }
  * { margin: 0; padding: 0; box-sizing: border-box; }
  html, body {
    width: 1200px;
    height: 816px;
    overflow: hidden;
    background: var(--backdrop);
  }
  .business-card {
    position: absolute;
    left: 80px;
    top: 108px;
    width: 1040px;
    height: 600px;
    border-radius: 28px;
    overflow: hidden;
    background: var(--card-white);
    font-family: "Aldrich", sans-serif;
    box-shadow: 0 10px 30px rgba(0,0,0,0.18);
  }
  .card-shapes {
    position: absolute;
    inset: 0;
  }
  .holder-name {
    position: absolute;
    left: 120px;
    top: 150px;
    color: var(--text-light);
    font-size: 26px;
    letter-spacing: 1px;
    text-transform: uppercase;
  }
  .holder-title {
    position: absolute;
    left: 120px;
    top: 184px;
    color: var(--text-light);
    font-size: 22px;
    letter-spacing: 1.5px;
  }
  .contact-line {
    position: absolute;
    left: 120px;
    color: var(--text-light);
    font-size: 21px;
    letter-spacing: 0.5px;
    line-height: 34px;
    white-space: nowrap;
  }
  .contact-phone { top: 336px; }
  .contact-web { top: 418px; }
  .contact-address { top: 500px; }
  .company-name {
    position: absolute;
    left: 860px;
    top: 300px;
    width: 560px;
    transform: translate(-50%, -50%) rotate(-90deg);
    color: var(--brand-red);
    font-size: 44px;
    letter-spacing: 5px;
    line-height: 58px;
    text-align: left;
    text-transform: uppercase;
  }
  .company-name span { display: block; }
</style>
</head>
<body>
  <div class="business-card">
    <svg class="card-shapes" width="1040" height="600" viewBox="0 0 1040 600">
      <polygon class="accent-band" fill="var(--brand-red)"
        points="0,0 625,0 700,95 700,470 570,600 0,600"/>
      <polygon class="dark-panel" fill="var(--card-charcoal)"
        points="0,0 590,0 660,110 660,450 535,600 0,600"/>

      <line class="divider" x1="120" y1="238" x2="560" y2="238" stroke="var(--brand-red)" stroke-width="5"/>
      <line class="divider" x1="50" y1="306" x2="520" y2="306" stroke="var(--brand-red)" stroke-width="5"/>

      <!-- person icon -->
      <g class="icon icon-person" transform="translate(80,190)">
        <circle r="22" fill="var(--brand-red)"/>
        <circle cy="-6" r="7" fill="#fff"/>
        <path d="M-12 12 Q-12 1 0 1 Q12 1 12 12 Z" fill="#fff"/>
      </g>
      <!-- phone icon -->
      <g class="icon icon-phone" transform="translate(80,370)">
        <circle r="22" fill="var(--brand-red)"/>
        <rect x="-7" y="-12" width="14" height="24" rx="3" fill="#fff"/>
        <rect x="-4.5" y="-8" width="9" height="14" fill="var(--brand-red)"/>
        <circle cy="9" r="1.5" fill="var(--brand-red)"/>
      </g>
      <!-- monitor icon -->
      <g class="icon icon-web" transform="translate(80,452)">
        <circle r="22" fill="var(--brand-red)"/>
        <rect x="-12" y="-10" width="24" height="16" rx="2" fill="none" stroke="#fff" stroke-width="2.5"/>
        <rect x="-2" y="6" width="4" height="4" fill="#fff"/>
        <rect x="-7" y="10" width="14" height="2.5" fill="#fff"/>
      </g>
      <!-- pin icon -->
      <g class="icon icon-pin" transform="translate(80,534)">
        <circle r="22" fill="var(--brand-red)"/>
        <path d="M0 13 L-8 1 A9.5 9.5 0 1 1 8 1 Z" fill="#fff"/>
        <circle cy="-4" r="3.5" fill="var(--brand-red)"/>
      </g>
    </svg>

    <div class="holder-name">Marcus Holt</div>
    <div class="holder-title">Managing Director</div>

    <div class="contact-line contact-phone">+61 7 55019284 · 0414093857<br>Fiji +679 8230519</div>
    <div class="contact-line contact-web">marcuswholt@tealnest-mail.com<br>tidewaterguest-consult.com</div>
    <div class="contact-line contact-address">PO Box 318 Coral Heath<br>4871 Qld</div>

    <div class="company-name">
      <span>Tidewater</span>
      <span>Guest</span>
      <span>Consulting</span>
    </div>
  </div>
</body>
</html>
```